Feral Horizon, a 3d voxel survival video game needs a card for gaming conventions

I am the lead developer for Feral Horizon http://www.FeralHorizon.example and need a business card to hand out at an indie gaming convention
The card would need to include the game name, website url, my name, position (Lead Developer), e-mail and phone number
The game is a 3d, voxel (with smooth terrain) based survival game with guns and wildlife. The main icon of the game would likely be a grizzly bear but I am willing to accept other designs too.
Attached is a media kit for the game with some images you can use but don't have to its just what little art I can provide. Anything on the website or from the video game can also be used. unrelated art can also be used.
Target Market(s)
Indie Developers/publishers at conferences
Industry/Entity Type
Games
Contact Information for Business Card
Name: Corwin Aldersby
Position: Lead Developer
E-mail: Pale_Lanterns@mailbox.example
Phone number: 555-207-3186

```html
<!DOCTYPE html>
<html lang="en">
<head>
<meta charset="utf-8">
<title>Feral Horizon – Business Card</title>
<link rel="stylesheet" href="https://fonts.googleapis.com/css2?family=Mulish:wght@600;700&display=swap">
<style>
  :root {
    --page: #ffffff;
    --front-top: #f1cf85;
    --front-mid: #9c8246;
    --front-bottom: #211803;
    --brand-wine: #8a4a55;
    --brand-tan: #b59a6e;
    --ink-light: #fbf8f0;
    --back-center: #b5a88c;
    --back-edge: #3f3b39;
    --silver: #d4d4d4;
    --art-light: #f2f2f2;
    --art-shade: #c4c4c4;
  }
  * { box-sizing: border-box; margin: 0; padding: 0; }
  html, body { width: 1038px; height: 1200px; overflow: hidden; background: var(--page); }
  body { position: relative; font-family: "Mulish", sans-serif; }

  .card {
    position: absolute;
    left: 22px;
    width: 994px;
    height: 567px;
    border-radius: 20px;
    overflow: hidden;
  }
  .card--front {
    top: 14px;
    background: linear-gradient(180deg, var(--front-top) 0%, var(--front-mid) 45%, var(--front-bottom) 100%);
  }
  .card--back {
    top: 617px;
    height: 568px;
    background: radial-gradient(ellipse 60% 70% at 50% 55%, var(--back-center) 0%, var(--back-edge) 100%);
  }

  .brand-mark {
    position: absolute;
    left: 70px; top: 24px;
    width: 148px; height: 148px;
    border-radius: 50%;
    background: var(--brand-tan);
  }
  .brand-name {
    position: absolute;
    font-weight: 700;
    font-variant: small-caps;
    letter-spacing: 1px;
    white-space: nowrap;
  }
  .card--front .brand-name {
    left: 250px; top: 42px;
    font-size: 82px;
    line-height: 1;
    color: var(--brand-wine);
  }

  .person {
    position: absolute;
    left: 20px; top: 318px;
    width: 420px;
    text-align: center;
    color: var(--ink-light);
  }
  .person__name { font-size: 41px; font-weight: 700; line-height: 1.1; }
  .person__role { font-size: 28px; font-weight: 700; margin-top: 16px; }

  .contacts { position: absolute; left: 440px; top: 240px; list-style: none; }
  .contact {
    display: flex; align-items: center;
    height: 92px;
    color: var(--ink-light);
    font-weight: 700;
    white-space: nowrap;
  }
  .contact__icon { width: 70px; height: 70px; flex: none; margin-right: 6px; }
  .contact__text { font-size: 29px; }
  .contact__text--email { font-size: 25px; }

  .card--back .brand-name {
    left: 0; right: 0; top: 20px;
    text-align: center;
    font-size: 82px;
    line-height: 1;
    color: var(--silver);
  }
  .hero-art {
    position: absolute;
    left: 182px; top: 139px;
    width: 630px; height: 318px;
    border-radius: 90px 60px 40px 40px;
    background: linear-gradient(135deg, var(--art-light) 0%, var(--art-shade) 100%);
  }
  .card--back .website {
    position: absolute;
    left: 0; right: 0; top: 500px;
    text-align: center;
    font-size: 33px;
    font-weight: 700;
    color: var(--ink-light);
  }
</style>
</head>
<body>

<section class="card card--front">
  <div class="brand-mark"></div>
  <div class="brand-name">Feral Horizon</div>

  <div class="person">
    <div class="person__name">Corwin Aldersby</div>
    <div class="person__role">Lead Developer</div>
  </div>

  <ul class="contacts">
    <li class="contact">
      <svg class="contact__icon" viewBox="0 0 70 70" fill="none" stroke="#fbf8f0" stroke-width="2">
        <path d="M14 10 L24 8 L30 22 L24 27 Q30 42 44 50 L50 44 L63 52 L60 62 Q46 68 30 52 Q10 32 14 10 Z"/>
        <path d="M38 18 Q50 20 52 32"/>
        <path d="M38 10 Q58 12 60 32"/>
      </svg>
      <span class="contact__text">:555-207-3186</span>
    </li>
    <li class="contact">
      <svg class="contact__icon" viewBox="0 0 70 70" fill="none" stroke="#fbf8f0" stroke-width="3">
        <rect x="2" y="14" width="66" height="44" fill="#fbf8f0" stroke="none"/>
        <path d="M4 16 L35 42 L66 16" stroke="#6b5a2e"/>
        <path d="M4 56 L28 36 M66 56 L42 36" stroke="#6b5a2e"/>
      </svg>
      <span class="contact__text contact__text--email">:Pale_Lanterns@mailbox.example</span>
    </li>
    <li class="contact">
      <svg class="contact__icon" viewBox="0 0 70 70" fill="none" stroke="#fbf8f0" stroke-width="1.5">
        <circle cx="35" cy="35" r="30"/>
        <ellipse cx="35" cy="35" rx="13" ry="30"/>
        <line x1="35" y1="5" x2="35" y2="65"/>
        <line x1="5" y1="35" x2="65" y2="35"/>
        <line x1="10" y1="20" x2="60" y2="20"/>
        <line x1="10" y1="50" x2="60" y2="50"/>
      </svg>
      <span class="contact__text">:www.FeralHorizon.example</span>
    </li>
  </ul>
</section>

<section class="card card--back">
  <div class="brand-name">Feral Horizon</div>
  <div class="hero-art" role="img" aria-label="Large faceted low-poly grizzly bear walking, in white and silver tones"></div>
  <div class="website">www.FeralHorizon.example</div>
</section>

</body>
</html>
```